BrickaFun Business Card

We need a business card design for our company. We sell construction-themed amusement rides for kids.

Contact Information for Business Card

Contact info on business card should include:
Dale Hurst
Co-Founder & COO
(833) 517-BRICKAF
Dale@brickafun.com
www.brickafun.com

```html
<!DOCTYPE html>
<html lang="en">
<head>
<meta charset="utf-8">
<title>BrickaFun Business Card</title>
<link href="https://fonts.googleapis.com/css2?family=Open+Sans:wght@400;600;700;800&display=swap" rel="stylesheet">
<style>
  :root {
    --stage: #5f6166;
    --card-white: #ffffff;
    --card-black: #050505;
    --orange: #ef5a24;
    --purple: #8e2b95;
    --ink: #2b2b2b;
    --rule: #555555;
  }
  * { margin: 0; padding: 0; box-sizing: border-box; }
  html, body { width: 1200px; height: 811px; overflow: hidden; }
  body {
    background: var(--stage);
    font-family: "Open Sans", Arial, sans-serif;
    display: flex;
    align-items: center;
    justify-content: center;
    gap: 48px;
  }
  .card {
    position: relative;
    width: 520px;
    height: 297px;
    overflow: hidden;
    box-shadow: 0 10px 28px rgba(0,0,0,.35);
  }
  /* Back */
  .card-back {
    background: var(--card-black);
    display: flex;
    align-items: center;
    justify-content: center;
  }
  .brand {
    display: flex;
    align-items: center;
    gap: 10px;
    font-weight: 800;
    color: var(--orange);
  }
  .brand-mark {
    width: 14px; height: 14px;
    background: var(--purple);
  }
  .card-back .brand { font-size: 46px; }
  .card-back .brand-mark { width: 26px; height: 26px; }

  /* Front */
  .card-front { background: var(--card-white); color: var(--ink); }
  .card-front .brand {
    position: absolute;
    left: 30px; top: 58px;
    font-size: 34px;
  }
  .person {
    position: absolute;
    right: 28px; top: 62px;
    text-align: right;
  }
  .person-name {
    color: var(--purple);
    font-weight: 700;
    font-size: 19px;
    line-height: 1.2;
  }
  .person-title { font-size: 11px; font-weight: 600; margin-top: 2px; }
  .divider-grey {
    position: absolute; left: 30px; top: 172px;
    width: 290px; height: 1px; background: var(--rule);
  }
  .divider-orange {
    position: absolute; left: 320px; top: 171px;
    width: 172px; height: 2px; background: var(--orange);
  }
  .contact {
    position: absolute;
    display: flex; align-items: center; gap: 7px;
    font-size: 11px; font-weight: 600;
  }
  .contact svg { width: 11px; height: 11px; fill: var(--orange); flex: none; }
  .contact-phone { left: 30px; top: 196px; }
  .contact-email { left: 212px; top: 184px; }
  .contact-web { right: 28px; top: 184px; }
  .band-base {
    position: absolute; left: 0; bottom: 0;
    width: 100%; height: 12px; background: var(--orange);
  }
  .band-orange {
    position: absolute; left: 250px; bottom: 12px;
    width: 210px; height: 22px; background: var(--orange);
  }
  .band-purple {
    position: absolute; left: 468px; bottom: 12px;
    width: 52px; height: 34px; background: var(--purple);
  }
</style>
</head>
<body>
  <div class="card card-back">
    <div class="brand"><span class="brand-mark"></span>BrickaFun</div>
  </div>

  <div class="card card-front">
    <div class="brand"><span class="brand-mark"></span>BrickaFun</div>

    <div class="person">
      <div class="person-name">Dale Hurst</div>
      <div class="person-title">Co-Founder &amp; COO</div>
    </div>

    <div class="divider-grey"></div>
    <div class="divider-orange"></div>

    <div class="contact contact-phone">
      <svg viewBox="0 0 12 12" aria-hidden="true"><path d="M3 0h6a1 1 0 0 1 1 1v10a1 1 0 0 1-1 1H3a1 1 0 0 1-1-1V1a1 1 0 0 1 1-1zm0 1.5v8h6v-8zm3 8.6a.6.6 0 1 0 0 1.2.6.6 0 0 0 0-1.2z"/></svg>
      (833) 517-BRICKAF
    </div>
    <div class="contact contact-email">
      <svg viewBox="0 0 12 12" aria-hidden="true"><path d="M0 2h12v8H0zm1 1v.4l5 3.2 5-3.2V3zm0 1.6V9h10V4.6L6 7.8z"/></svg>
      Dale@brickafun.com
    </div>
    <div class="contact contact-web">
      <svg viewBox="0 0 12 12" aria-hidden="true"><circle cx="6" cy="6" r="6"/><circle cx="6" cy="6" r="2.4" fill="#fff"/></svg>
      www.brickafun.com
    </div>

    <div class="band-orange"></div>
    <div class="band-purple"></div>
    <div class="band-base"></div>
  </div>
</body>
</html>
```